In-Aisle Customer Special Order Process and FAQ

This infographic/brochure is intended for owners of Birchwell Supply retail stores who I'm looking to inform about a new process for managing customer special orders. There will be two pages to this infographic / FAQ.

The first page I am looking for a very unique and creative way to educate them on the steps needed to process a customer special order. The two PowerPoint slides I attached is the content for this process. I'm looking to illustrate this information in a very fun and differentiated way that will catch the Birchwell Supply owners' attention! It must stand out. Right now, the way that it is laid out is boring, unattractive to look at, and too cluttered. I will need all this content, but it will need to be formatted and designed in a much, much better way. Note that step 7 could be either an in-store pick-up or deliver (not both), so the infographic must make that clear.

* Use logos provided. The red vest logo is the mobile app

The second page is a frequently asked question section. This should be in a two column form and match the design of the first page.

Feel free to use some of the images I provided, but not necessary.

Target Market(s)

Birchwell Supply Store Owners

Font styles to use
Serif

Colors
EB3D1F
EC4F4E
F09395
F8D3D4
FCEDEE

Requirements
Must have
• Birchwell Supply red and black colors; 8-1/2x11; 2 pages, front and back, Super creative, different looking, eye catching, use all the content I provided. Must include each step, system touchpoints, Lead/location, actions, and outcomes; size 11 font or bigger
Nice to have
• Some of the photos I sent

```html
<!DOCTYPE html>
<html lang="en">
<head>
<meta charset="utf-8">
<title>In-Aisle Customer Special Order Process</title>
<link href="https://fonts.googleapis.com/css2?family=Playfair+Display:wght@600;700&family=Open+Sans:wght@400;600;700;800&display=swap" rel="stylesheet">
<style>
:root{
  --backdrop:#efc9e3;
  --red:#e31b23;
  --red-deep:#b5121b;
  --ink:#121212;
  --card:#1e1e1e;
  --text:#d9d9d9;
  --muted:#a9a9a9;
  --white:#ffffff;
  --s1:#e31b23;
  --s2:#f07a1a;
  --s3:#d7197f;
  --s4:#24449a;
  --s5:#1ea3d8;
  --s6:#18a38f;
  --s7:#7dc242;
}
*{box-sizing:border-box;margin:0;padding:0}
html,body{width:1200px;height:2662px;overflow:hidden}
body{background:var(--backdrop);font-family:"Open Sans",Arial,sans-serif;color:var(--text);position:relative}
.page{position:absolute;left:152px;width:896px;background:var(--ink);overflow:hidden;box-shadow:0 6px 18px rgba(0,0,0,.25)}
.page-process{top:117px;height:1180px}
.page-faq{top:1366px;height:1196px}

/* header art */
.hero-photo{position:absolute;left:0;top:0;width:896px;height:470px;background:linear-gradient(120deg,#5d4b3c 0%,#8a7a6a 40%,#b9aea2 70%,#6b625a 100%)}
.hero-shapes{position:absolute;left:0;top:0}
.brand{position:absolute;left:28px;top:26px;display:flex;align-items:center;gap:10px}
.brand-square{width:30px;height:30px;background:var(--white)}
.brand-name{font-family:"Open Sans",sans-serif;font-weight:800;font-size:15px;color:var(--white);line-height:1.05;text-transform:uppercase}
.brand-name small{display:block;font-size:10px;letter-spacing:.5px}
.process-title{position:absolute;left:40px;top:190px;width:380px;font-family:"Playfair Display",Georgia,serif;font-weight:700;font-size:42px;line-height:1.2;color:var(--white)}

/* step cards */
.step{position:absolute;width:190px;background:var(--card);padding:10px 10px 8px;overflow:hidden;font-size:8.3px;line-height:1.32}
.step-row-top{top:455px;height:280px}
.step-row-bottom{top:852px;height:262px}
.step h2{font-family:"Open Sans",sans-serif;font-size:12px;font-weight:700;color:var(--white);margin-bottom:6px}
.step h2 span{font-size:8px;font-weight:600;color:var(--muted)}
.step .meta{color:var(--white);margin-bottom:3px}
.step .meta b{font-weight:700}
.step h3{font-size:8.6px;font-weight:700;color:var(--white);margin:5px 0 2px}
.step ul{list-style:none}
.step li{position:relative;padding-left:8px;color:var(--text)}
.step li::before{content:"";position:absolute;left:1px;top:4px;width:3px;height:3px;background:var(--muted);border-radius:50%}

.markers{position:absolute;left:0;top:725px}
.marker-num{font-family:"Playfair Display",Georgia,serif;font-weight:700;font-size:30px;fill:var(--white)}

/* footer page 1 */
.process-footer{position:absolute;left:0;bottom:0;width:896px;height:44px;background:#0b0b0b;display:flex;align-items:center}
.footer-tab{height:44px;background:var(--red);display:flex;align-items:center;padding:0 18px;font-family:"Playfair Display",Georgia,serif;font-weight:700;font-size:17px;color:var(--white);width:200px}
.footer-contact{flex:1;text-align:center;font-size:12px;color:var(--white)}
.footer-net{height:44px;width:170px;background:var(--red);display:flex;align-items:center;justify-content:center;font-weight:800;font-size:20px;color:var(--white)}

/* FAQ page */
.faq-photo{position:absolute;left:0;top:0;width:896px;height:340px;background:linear-gradient(180deg,#6e2a22 0%,#8f5a4a 45%,#4b3a33 75%,var(--ink) 100%)}
.faq-title{position:absolute;left:0;top:300px;width:896px;text-align:center;font-family:"Playfair Display",Georgia,serif;font-weight:700;font-size:40px;color:var(--white)}
.faq-grid{position:absolute;left:32px;top:380px;width:832px;display:grid;grid-template-columns:1fr 1fr;column-gap:28px;row-gap:14px}
.faq-item{display:grid;grid-template-columns:22px 1fr;column-gap:10px;height:132px;overflow:hidden}
.faq-icon{width:22px;height:22px;border-radius:50%;background:var(--red);color:var(--white);font-weight:800;font-size:13px;display:flex;align-items:center;justify-content:center}
.faq-q{font-weight:700;font-size:10.5px;line-height:1.35;color:var(--white);margin-bottom:6px}
.faq-a{font-size:9.3px;line-height:1.45;color:var(--muted)}
.faq-footer{position:absolute;left:0;bottom:0;width:896px;height:58px;background:#0b0b0b;display:flex;align-items:center;padding:0 24px}
.faq-brand{display:flex;align-items:center;gap:8px;width:210px}
.faq-brand .brand-square{width:22px;height:22px}
.faq-brand .brand-name{font-size:11px}
.faq-contact{flex:1;height:30px;background:var(--red);display:flex;align-items:center;justify-content:center;gap:46px;font-size:11px;color:var(--white);font-weight:600}
.faq-net{width:150px;text-align:right;font-weight:800;font-size:20px;color:var(--white)}
</style>
</head>
<body>

<section class="page page-process">
  <div class="hero-photo" role="img" aria-label="Photo of a store associate in a red vest showing a product box to a customer in an aisle"></div>
  <svg class="hero-shapes" width="896" height="520" viewBox="0 0 896 520" aria-hidden="true">
    <polygon points="0,0 520,0 380,430 0,470" fill="#e31b23"/>
    <polygon points="0,470 380,430 896,360 896,520 0,520" fill="#121212"/>
    <polygon points="0,462 380,422 896,352 896,360 380,430 0,470" fill="#ffffff" opacity=".85"/>
  </svg>
  <div class="brand">
    <div class="brand-square"></div>
    <div class="brand-name">Birchwell Supply<small>Store Systems &amp; Operations</small></div>
  </div>
  <h1 class="process-title">In-Aisle Customer Special Order Process</h1>

  <article class="step step-row-top" style="left:32px">
    <h2>Order Entry</h2>
    <p class="meta"><b>System Touchpoint:</b> BirchNet or Mobile App</p>
    <p class="meta"><b>Lead / Location:</b> Sales Associate / In-Aisle</p>
    <h3>Actions</h3>
    <ul><li>Create Store Reserve or Customer Priority Order</li><li>Add direct assembly and/or fee for delivery</li><li>Verify item order multiple</li><li>Communicate ETA</li></ul>
    <h3>Outcomes</h3>
    <ul><li>Order transmitted to the RSC</li><li>Order confirmation sent to customer</li><li>Order lands in Harbor POS as a Special Order</li><li>Updates BirchNet Deliveries &amp; Services App</li></ul>
  </article>

  <article class="step step-row-top" style="left:246px">
    <h2>Receive</h2>
    <p class="meta"><b>System Touchpoint:</b> Mobile App</p>
    <p class="meta"><b>Lead / Location:</b> Designated Receivers in Back Room</p>
    <h3>Actions</h3>
    <ul><li>Pull special orders receipt and tag feature</li><li>Associate items with Special Orders</li><li>Write pick ticket</li></ul>
    <h3>Outcomes</h3>
    <ul><li>Prepared product for receiving and staging</li></ul>
  </article>

  <article class="step step-row-top" style="left:460px">
    <h2>Stage</h2>
    <p class="meta"><b>System Touchpoint:</b> Mobile App</p>
    <p class="meta"><b>Lead / Location:</b> Designated Staff / Staging Area</p>
    <h3>Actions</h3>
    <ul><li>Move each directly received item to a visible staging area, sorted by order</li><li>Cross-reference staging area against product</li><li>Review orders via fulfillment / order status</li></ul>
    <h3>Outcomes</h3>
    <ul><li>The store sets up notification sent to customer</li><li>Once staged or delivered, orders are placed in Order Prep on the mobile app</li></ul>
  </article>

  <article class="step step-row-top" style="left:674px">
    <h2>In-Store Pick-Up Or Deliver</h2>
    <p class="meta"><b>System Touchpoint:</b> Mobile App</p>
    <p class="meta"><b>Lead / Location:</b> Cashier or Sales Associate</p>
    <h3>Pick-Up Actions</h3>
    <ul><li>Complete pick-up via the Ready for Pickup feature</li><li>Locate order in staging area</li><li>Validate invoice and order paid</li></ul>
    <h3>Deliver Actions</h3>
    <ul><li>Route order to Needs Delivery feature</li><li>Contact customer to confirm time window</li><li>Validate invoice and order paid</li><li>Take signature / photo for unattended delivery</li></ul>
    <h3>Outcomes</h3>
    <ul><li>Closed order &amp; happy customer</li></ul>
  </article>

  <svg class="markers" width="896" height="130" viewBox="0 0 896 130" aria-hidden="true">
    <polygon points="32,0 222,0 222,45 127,85 32,45" fill="#e31b23"/>
    <text class="marker-num" x="127" y="48" text-anchor="middle">01</text>
    <polygon points="246,0 436,0 436,45 341,85 246,45" fill="#d7197f"/>
    <text class="marker-num" x="341" y="48" text-anchor="middle">03</text>
    <polygon points="460,0 650,0 650,45 555,85 460,45" fill="#1ea3d8"/>
    <text class="marker-num" x="555" y="48" text-anchor="middle">05</text>
    <polygon points="674,0 864,0 864,45 769,85 674,45" fill="#7dc242"/>
    <text class="marker-num" x="769" y="48" text-anchor="middle">07</text>
    <polygon points="139,85 234,45 329,85 329,127 139,127" fill="#f07a1a"/>
    <text class="marker-num" x="234" y="115" text-anchor="middle">02</text>
    <polygon points="353,85 448,45 543,85 543,127 353,127" fill="#24449a"/>
    <text class="marker-num" x="448" y="115" text-anchor="middle">04</text>
    <polygon points="567,85 662,45 757,85 757,127 567,127" fill="#18a38f"/>
    <text class="marker-num" x="662" y="115" text-anchor="middle">06</text>
  </svg>

  <article class="step step-row-bottom" style="left:139px">
    <h2>Complete POS Trx</h2>
    <p class="meta"><b>System Touchpoint:</b> Harbor POS</p>
    <p class="meta"><b>Lead / Location:</b> Cashier at POS / Hub</p>
    <h3>Actions</h3>
    <ul><li>Search in Harbor POS by customer phone #</li><li>Import order into POS</li><li>Take item deposit</li><li>Process order: items / delivery fees separately</li><li>Provide receipt to customer and thank them</li></ul>
    <h3>Outcomes</h3>
    <ul><li>Creates SO in Harbor POS, if it hadn't already</li><li>Committed Qty updated</li><li>Deposit amount recorded in Harbor POS</li></ul>
  </article>

  <article class="step step-row-bottom" style="left:353px">
    <h2>Invoice</h2>
    <p class="meta"><b>System Touchpoint:</b> Harbor POS</p>
    <p class="meta"><b>Lead / Location:</b> Back Office Store Associate / Back Office</p>
    <h3>Actions</h3>
    <ul><li>Reference order stock invoice</li><li>Show outstanding balance due</li><li>Staple invoice to pick sheet</li></ul>
    <h3>Outcomes</h3>
    <ul><li>Qty. On Hand decreased</li><li>Committed Qty relieved</li><li>Sales transaction recorded</li></ul>
  </article>

  <article class="step step-row-bottom" style="left:567px">
    <h2>Assembly <span>(when applicable)</span></h2>
    <p class="meta"><b>System Touchpoint:</b> Mobile App</p>
    <p class="meta"><b>Lead / Location:</b> Designated Staff / Staging Area</p>
    <h3>Actions</h3>
    <ul><li>Physically assemble product</li><li>Assign product Ready for Pickup</li></ul>
    <h3>Outcomes</h3>
    <ul><li>Assembly task closed in Mobile App, notification sent to customer</li><li>Ready for Pickup or Delivery status set in mobile app</li><li>Delivery notification sent to customer on delivery date</li></ul>
  </article>

  <footer class="process-footer">
    <div class="footer-tab">Miscellaneous</div>
    <div class="footer-contact">Contact - Back Office Store Associates / Back Office</div>
    <div class="footer-net">BirchNet</div>
  </footer>
</section>

<section class="page page-faq">
  <div class="faq-photo" role="img" aria-label="Photo of a smiling customer talking with a store associate in a red vest"></div>
  <h1 class="faq-title">Frequently Asked Questions</h1>
  <div class="faq-grid">
    <div class="faq-item"><div class="faq-icon">?</div><div><p class="faq-q">What is meant by "In-Aisle Customer Special Orders" and what kind of impact can they have on my business?</p><p class="faq-a">Special orders are items ordered for a customer right in the aisle, on the spot. Handled well, they grow sales, win repeat visits and build trust, since the customer leaves knowing exactly when the product arrives.</p></div></div>
    <div class="faq-item"><div class="faq-icon">?</div><div><p class="faq-q">My current special order process is slow and cumbersome. How has the process become simpler to manage?</p><p class="faq-a">With the mobile app the order is created in the aisle and flows straight to receiving, staging and pick-up. Fewer hand-offs and fewer screens mean less paperwork and faster answers for your team.</p></div></div>
    <div class="faq-item"><div class="faq-icon">?</div><div><p class="faq-q">We use the mobile for special orders, but there are times in the process it is more convenient to use a computer terminal. Have there been any changes here?</p><p class="faq-a">Yes. Orders can now be created or reviewed on BirchNet from any terminal, and they stay in sync with the mobile app so staff can switch devices without losing a step.</p></div></div>
    <div class="faq-item"><div class="faq-icon">?</div><div><p class="faq-q">Super important to the special orders is communicating back to the customer the status of their order. How is this accomplished with the experience?</p><p class="faq-a">Customers get automatic notices when the order is placed, ready for pick-up or out for delivery, so they always know where things stand without calling the store.</p></div></div>
    <div class="faq-item"><div class="faq-icon">?</div><div><p class="faq-q">I hear different things. When is the right time to invoice the special order?</p><p class="faq-a">Invoice once the product is received and staged. This keeps on-hand counts accurate and lets the balance due be collected at pick-up or delivery.</p></div></div>
    <div class="faq-item"><div class="faq-icon">?</div><div><p class="faq-q">I see the value in the process, but I would like more understanding to implement. What do I do?</p><p class="faq-a">Step-by-step guides and short training videos are on BirchNet under Store Systems. Your field team can also walk your staff through a live order.</p></div></div>
    <div class="faq-item"><div class="faq-icon">?</div><div><p class="faq-q">From time to time, customers call in asking for updates to their special orders, and we don't have a good process for checking efficiently. Has anything changed?</p><p class="faq-a">Order status is now visible in the mobile app and on BirchNet. Search by customer phone number to see the ETA and current step in seconds.</p></div></div>
    <div class="faq-item"><div class="faq-icon">?</div><div><p class="faq-q">What are some important but underutilized best practices I should be doing with every special order to help ensure an effective process?</p><p class="faq-a">Always confirm the ETA, take a deposit, label staged items clearly and review open orders weekly. Small habits keep orders from slipping through.</p></div></div>
    <div class="faq-item"><div class="faq-icon">?</div><div><p class="faq-q">I reviewed the best practice. Why do I need to take a 100% deposit?</p><p class="faq-a">A full deposit protects the store from unclaimed orders and non-returnable items, and it makes pick-up quicker for the customer.</p></div></div>
    <div class="faq-item"><div class="faq-icon">?</div><div><p class="faq-q">Who do I contact with any further questions and support?</p><p class="faq-a">Reach the Store Systems and Operations team at +1 555-014-2290 or storesystems@birchwellsupply.com.</p></div></div>
  </div>
  <footer class="faq-footer">
    <div class="faq-brand"><div class="brand-square"></div><div class="brand-name">Birchwell Supply<small>Store Systems &amp; Operations</small></div></div>
    <div class="faq-contact"><span>&#9742; +1 555-014-2290</span><span>&#9993; storesystems@birchwellsupply.com</span></div>
    <div class="faq-net">BirchNet</div>
  </footer>
</section>

</body>
</html>
```